Patient Card - Eating Healthy on a Budget

We are looking for a 2-sided handout design for patients that need guidance on how to eat healthy on a budget. Content attached and photos for each recipe.
Size: 5.5” x 8.5” - if this size doesn't work, i'm open to recommendations here!
Lumbra Logo attached
Brand colors:
Terracotta - #b4734e
C=25 M=58 Y=74 K=8
Green - #788f70
C=58 M=32 Y=65 K=9
Blue - #5c7091
C=71 M=53 Y=26 K=4
Tan - #f3dcba
C=4 M=12 Y=28 K=0
Light tan (mainly used for background colors) - #f2eee4
C=4 M=4 Y=9 K=0
Fonts:
- We use Domaine Text for headlines and GT America fonts for body copy; weights can vary for design purposes.

```html
<!DOCTYPE html>
<html lang="en">
<head>
<meta charset="utf-8">
<title>Lumbra Health Card – Budget-Friendly Recipes</title>
<link rel="stylesheet" href="https://fonts.googleapis.com/css2?family=DM+Serif+Display&family=Barlow+Semi+Condensed:wght@400;500;600&display=swap">
<style>
  :root {
    --terracotta: #b4734e;
    --green: #788f70;
    --green-band: #6f8a68;
    --paper: #f7f4ea;
    --ink: #1f1f1f;
    --rule: #2a2a2a;
    --white: #ffffff;
  }
  * { box-sizing: border-box; margin: 0; padding: 0; }
  html, body { width: 847px; height: 1200px; overflow: hidden; }
  body {
    background: var(--paper);
    font-family: "Barlow Semi Condensed", "Arial Narrow", sans-serif;
    color: var(--ink);
    position: relative;
  }
  .card { position: absolute; inset: 0; background: var(--paper); }
  .card-header {
    position: absolute; left: 0; top: 0; width: 847px; height: 107px;
    background: var(--green-band);
    display: flex; align-items: center; justify-content: center;
  }
  .card-title {
    font-family: "DM Serif Display", Georgia, serif;
    font-weight: 400; color: var(--white); font-size: 29px; letter-spacing: -0.2px;
  }
  .recipe-title {
    position: absolute; left: 75px;
    font-family: "DM Serif Display", Georgia, serif;
    font-weight: 400; color: var(--terracotta);
    font-size: 30px; line-height: 32px;
  }
  .title-rule { position: absolute; left: 75px; width: 431px; height: 3px; }
  .section-label {
    position: absolute; left: 77px;
    font-weight: 600; color: var(--green); font-size: 17px;
  }
  .ingredients {
    position: absolute; left: 77px; width: 400px;
    list-style: none; font-size: 16.5px; line-height: 23px;
  }
  .ingredients li { position: relative; padding-left: 11px; }
  .ingredients li::before { content: "•"; position: absolute; left: 0; }
  .ingredients li.no-bullet::before { content: ""; }
  .ingredients li.wrap { line-height: 21px; margin-bottom: 2px; }
  .dish-photo {
    position: absolute; border-radius: 50%;
    border: 9px solid var(--white);
    box-shadow: 0 6px 14px rgba(0,0,0,0.18);
  }
  .dish-photo.oats {
    left: 530px; top: 160px; width: 248px; height: 238px;
    background: radial-gradient(circle at 55% 45%, #f2e7c4 0 22%, #cfc5b4 40%, #bdb3a4 100%);
  }
  .dish-photo.pasta {
    left: 524px; top: 580px; width: 262px; height: 250px;
    background: radial-gradient(circle at 50% 50%, #e1ae45 0 35%, #cf9330 70%, #b97d28 100%);
  }
  .method-box {
    position: absolute; left: 75px; width: 696px;
    border: 1.2px solid var(--rule);
    padding: 5px 12px 6px 13px;
    font-size: 12.4px; line-height: 15px;
  }
  .method-box h3 { font-size: 13px; font-weight: 600; }
  .method-box .step { font-weight: 400; }
  .method-box .step b { font-weight: 600; }
</style>
</head>
<body>
<main class="card">
  <header class="card-header">
    <h1 class="card-title">Dietitian-Approved and Budget-Friendly Recipes</h1>
  </header>

  <!-- Recipe 1 -->
  <h2 class="recipe-title" style="top:156px;">Peanut Butter Overnight<br>Oats with Banana</h2>
  <svg class="title-rule" style="top:224px;" viewBox="0 0 431 3" aria-hidden="true"><polygon points="0,0 431,0 415,3 0,3" fill="var(--green)"/></svg>
  <div class="section-label" style="top:239px;">Ingredients</div>
  <ul class="ingredients" style="top:262px;">
    <li>1 cup milk of your choice</li>
    <li>1/2 cup Rolled Oats</li>
    <li>1 teaspoon Vanilla Extract</li>
    <li class="wrap">2 tablespoons Unsweetened Peanut Butter (or nut butter of your choice)</li>
    <li>1 Banana</li>
    <li>1 tablespoon Ground Flaxseed (optional)</li>
  </ul>
  <div class="dish-photo oats" role="img" aria-label="Bowl of peanut butter overnight oats topped with banana slices"></div>
  <section class="method-box" style="top:443px; height:78px;">
    <h3>Intructions</h3>
    <p>In a medium bowl, stir together the rmilk, oats, and vanilla. Add the peanut butter and stir to combine. Divide between two wide-mouth jars, cover, and refrigerate for at least 4 hours or overnight. Before serving, peel and slice banana and top oats, dividing evenly.</p>
  </section>

  <!-- Recipe 2 -->
  <h2 class="recipe-title" style="top:571px;">One Pot Pumpkin<br>Parmesan Pasta</h2>
  <svg class="title-rule" style="top:640px;" viewBox="0 0 431 3" aria-hidden="true"><polygon points="0,0 431,0 415,3 0,3" fill="var(--green)"/></svg>
  <div class="section-label" style="top:656px;">Ingredients</div>
  <ul class="ingredients" style="top:679px;">
    <li>1/2 cup Pumpkin Puree, 100% Pumpkin</li>
    <li class="no-bullet wrap">12 ounces (4 cups) Pasta, such as Penne or Rotini (whole wheat pasta recommended)</li>
    <li>1/8 teaspoon Ground Nutmeg</li>
    <li>1 teaspoon Garlic Powder</li>
    <li>1 teaspoon Onion Powder</li>
    <li>1/4 teaspoon Kosher Salt</li>
    <li>1/4 cup Low Fat Cream Cheese</li>
    <li>1/2 cup Grated Parmesan</li>
    <li>1/4 teaspoon Crushed Red Pepper Flakes (optional)</li>
  </ul>
  <div class="dish-photo pasta" role="img" aria-label="Bowl of penne in pumpkin sauce topped with parmesan and pepper flakes"></div>
  <section class="method-box" style="top:937px; height:218px;">
    <h3>Instructions</h3>
    <p class="step"><b>1.</b> Prepare Ingredients</p>
    <p>Measure 1/2 cup of pumpkin puree. Reserve remainder for another use.</p>
    <p class="step"><b>2.</b> Cook Pasta</p>
    <p>Add pasta, pumpkin puree, ground nutmeg, garlic powder, onion powder, salt, and 5 cups of water to a large pot. Bring to a boil over high heat. Once boiling, reduce heat to medium-high and cook, stirring frequently to prevent pasta from sticking, until pasta is al dente and liquid is absorbed, 9-11 minutes. Remove pot from heat and set aside to cool slightly, 5 minutes.</p>
    <p class="step"><b>3.</b> Finish</p>
    <p>To pot with pasta, add cream cheese and half of parmesan and stir to fully combine. Divide pumpkin pasta among serving bowls. Top with remaining parmesan and a sprinkle of crushed red pepper flakes if you like a bit of heat. Enjoy!</p>
  </section>
</main>
</body>
</html>
```